Book and Ebook Cover for my Upcoming Book

About the Book
------------------
I need a book, ebook and if possible audio cover design for my upcoming book - Lanterns & Larkspur. This is my first book and really looking for a great book cover. The book is about my story, living with Mental Health and how to reclaim control of your life.

Quillbarrow
-----------
I am using quillbarrow.com to self-publish my book so in case of any design-related questions you can just search info on their website.

I have an initial theme I am thinking for the design book cover which I have attached. You can use this as a starting point.

Idea for the theme
---------------------
I am thinking about a phoenix to represent rising from the ashes and rebirth. The phoenix motif will be continued throughout the interior pages of the book. I'd like the cover of the book to be minimal, white with gold lettering, and maybe incorporating wings? feel free to play around with the idea and up for suggestions.

If you can think of something along these lines and make it a lot better that would be great.

What I need
---------------
The book is complete and is Trim size is 6.14 x 9.21” (234 x 156mm). I would need-
1. Book Cover
2. Back & Spine Design
3. Source File
4. Ebook Cover
5. Need multiple revisions to get the best possible outcome
6. My name and book title should also on the front cover
7. The book title should be bigger size than the subtitle

If you can give me Audiobook cover, I would love that as well and can pay extra for it if needed.

I love this for the interior phoenix motif:
https://craftbazaarly.com/InkMoth/7720458-Watercolor-Heron-Clipart-Set#fullscreen

The only other actual book cover I found online that remotely relates to what I am looking for is this -
https://www.lookfinder.example/url?sa=i&url=https%3A%2F%2Fpixelmoor.com%2Fvantrell&psig=QxTrPLm3KZ9vBwE2dYcN41HoJuSA&ust=1598415525610000&source=images&cd=vfe&ved=0CAIQjRxqFwoTCPD_toPAtesCFQAAAAAdAAAAABAD

Target Market(s)

Personal Development
Mental health

Requirements
Must have
• 1. Book Cover
2. Back & Spine Design
3. Source File
4. Ebook Cover
Nice to have
• Audiobook cover as I eventually will be releasing the audio version of the book

```html
<!DOCTYPE html>
<html lang="en">
<head>
<meta charset="utf-8">
<title>Lanterns &amp; Larkspur — Cover Wrap</title>
<link rel="stylesheet" href="https://fonts.googleapis.com/css2?family=Cinzel:wght@400;600;700&family=Roboto+Condensed:wght@400&display=swap">
<style>
  :root {
    --backdrop: #232323;
    --paper: #ffffff;
    --paper-edge: #e9e9e9;
    --gold-dark: #7d5a1c;
    --gold-mid: #b88a34;
    --gold-light: #e6c777;
    --gold-gradient: linear-gradient(180deg, #9a7128 0%, #d9b660 45%, #8c6320 100%);
    --ink: #2b2b2b;
    --ink-soft: #555555;
    --rule: #b9b9b9;
    --photo-grey: #4a4a4a;
    --title-font: "Cinzel", Georgia, serif;
    --body-font: "Roboto Condensed", Arial, sans-serif;
  }
  * { box-sizing: border-box; margin: 0; padding: 0; }
  html, body { width: 1200px; height: 1200px; overflow: hidden; }
  body { background: var(--backdrop); position: relative; }

  .cover-wrap {
    position: absolute; left: 50px; top: 210px;
    width: 1100px; height: 780px;
    display: flex;
  }
  .panel { position: relative; height: 100%; background: var(--paper); }
  .back-cover { width: 520px; }
  .spine { width: 60px; background: linear-gradient(90deg, var(--paper-edge), var(--paper) 20%, var(--paper) 80%, var(--paper-edge)); }
  .front-cover { width: 520px; }

  .gold-text {
    background: var(--gold-gradient);
    -webkit-background-clip: text; background-clip: text;
    color: transparent;
  }

  /* Front cover */
  .book-title {
    position: absolute; left: 0; right: 0;
    font-family: var(--title-font); font-weight: 600;
    text-align: center; font-size: 66px; letter-spacing: 1px; line-height: 1;
  }
  .title-line-one { top: 58px; }
  .title-line-two { top: 172px; }
  .title-ampersand-row {
    position: absolute; left: 60px; right: 60px; top: 122px;
    display: flex; align-items: center; gap: 18px;
  }
  .title-ampersand-row .rule { flex: 1; height: 1px; background: linear-gradient(90deg, transparent, var(--rule)); }
  .title-ampersand-row .rule.right { background: linear-gradient(90deg, var(--rule), transparent); }
  .ampersand { font-family: var(--title-font); font-size: 40px; color: var(--ink-soft); line-height: 1; }

  .phoenix-emblem {
    position: absolute; left: 70px; top: 290px; width: 380px; height: 270px;
    background: radial-gradient(ellipse 50% 48% at 50% 45%, var(--gold-light) 0%, var(--gold-mid) 45%, rgba(184,138,52,0.25) 75%, rgba(255,255,255,0) 100%);
  }
  .subtitle {
    position: absolute; left: 0; right: 0; top: 590px;
    font-family: var(--title-font); font-size: 19px; color: var(--ink-soft);
    text-align: center; line-height: 1.3; letter-spacing: 0.5px;
  }
  .author-name {
    position: absolute; left: 0; right: 0; top: 690px;
    font-family: var(--title-font); font-weight: 600; font-size: 40px;
    text-align: center; letter-spacing: 1px;
  }

  /* Spine */
  .spine-text {
    position: absolute; left: 50%; top: 50%;
    transform: translate(-50%, -50%) rotate(90deg);
    width: 740px; display: flex; justify-content: space-between; align-items: center;
    font-family: var(--title-font); font-weight: 600; font-size: 20px; white-space: nowrap;
  }
  .spine-amp { color: var(--gold-mid); }

  /* Back cover */
  .back-title {
    position: absolute; left: 0; right: 0; top: 50px;
    font-family: var(--title-font); font-weight: 600; font-size: 30px;
    text-align: center; letter-spacing: 0.5px;
  }
  .back-title-rule {
    position: absolute; left: 40px; right: 40px; top: 100px; height: 1px;
    background: linear-gradient(90deg, transparent, var(--rule) 20%, var(--rule) 80%, transparent);
  }
  .blurb {
    position: absolute; left: 40px; right: 40px; top: 122px;
    font-family: var(--body-font); font-size: 13.5px; line-height: 1.38;
    color: var(--ink); text-align: justify;
  }
  .blurb p + p { margin-top: 16px; }
  .back-emblem-row {
    position: absolute; left: 40px; right: 40px; top: 418px; height: 80px;
    display: flex; align-items: center; gap: 16px;
  }
  .back-emblem-row .rule { flex: 1; height: 1px; background: linear-gradient(90deg, transparent, var(--rule)); }
  .back-emblem-row .rule.right { background: linear-gradient(90deg, var(--rule), transparent); }
  .small-phoenix {
    width: 100px; height: 80px;
    background: radial-gradient(ellipse 50% 46% at 50% 45%, var(--gold-light) 0%, var(--gold-mid) 45%, rgba(184,138,52,0.2) 78%, rgba(255,255,255,0) 100%);
  }
  .author-photo {
    position: absolute; left: 0; top: 525px; width: 110px; height: 160px;
    background: var(--photo-grey);
  }
  .about-heading {
    position: absolute; left: 130px; right: 40px; top: 532px;
    font-family: var(--title-font); font-size: 22px; color: var(--ink);
    text-align: center; letter-spacing: 0.5px;
  }
  .about-text {
    position: absolute; left: 130px; right: 40px; top: 566px;
    font-family: var(--body-font); font-size: 13.5px; line-height: 1.38;
    color: var(--ink); text-align: justify;
  }
</style>
</head>
<body>
  <main class="cover-wrap">
    <section class="panel back-cover">
      <h2 class="back-title gold-text">Lanterns &amp; Larkspur</h2>
      <div class="back-title-rule"></div>
      <div class="blurb">
        <p>Lorem Ipsum is simply dummy text of the printing and typesetting industry. Lorem Ipsum has been the industry's standard dummy text ever since the 1500s, when an unknown printer took a galley of type and scrambled it to make a type specimen book. It has survived not only five centuries, but also the leap into electronic typesetting, remaining essentially unchanged. It was popularised in the 1960s with the release of Tessamark sheets containing Lorem Ipsum passages, and more recently with desktop publishing software like Verdane PageSmith including versions of Lorem Ipsum.</p>
        <p>Lorem Ipsum is simply dummy text of the printing and typesetting industry. Lorem Ipsum has been the industry's standard dummy text ever since the 1500s, when an unknown printer took a galley of type and scrambled it to make a type specimen book. It has survived not only five centuries, but also the leap into electronic typesetting, remaining essentially unchanged.</p>
      </div>
      <div class="back-emblem-row">
        <span class="rule"></span>
        <div class="small-phoenix" role="img" aria-label="Small gold phoenix with spread wings"></div>
        <span class="rule right"></span>
      </div>
      <div class="author-photo" role="img" aria-label="Author portrait photo"></div>
      <h3 class="about-heading">About the Author</h3>
      <p class="about-text">Lorem Ipsum is simply dummy text of the printing and typesetting industry. Lorem Ipsum has been the industry's standard dummy text ever since the 1500s, when an unknown printer took a galley of type and scrambled it to make a type specimen book. It has survived not only five centuries, but also the leap into electronic typesetting, remaining essentially unchanged.</p>
    </section>

    <section class="panel spine">
      <div class="spine-text">
        <span class="gold-text">LANTERNS <span class="spine-amp">&amp;</span> LARKSPUR</span>
        <span class="gold-text">MIREVAL TK</span>
      </div>
    </section>

    <section class="panel front-cover">
      <h1>
        <span class="book-title title-line-one gold-text">LANTERNS</span>
        <span class="title-ampersand-row"><span class="rule"></span><span class="ampersand">&amp;</span><span class="rule right"></span></span>
        <span class="book-title title-line-two gold-text">LARKSPUR</span>
      </h1>
      <div class="phoenix-emblem" role="img" aria-label="Gold phoenix rising with wings spread wide"></div>
      <p class="subtitle">HOW TO RECLAIM<br>CONTROL OF YOUR LIFE</p>
      <p class="author-name gold-text">MIREVAL TK</p>
    </section>
  </main>
</body>
</html>
```